Business card design needed

am looking for a fun and funky design to match our moto, seriously fun swimwear and fashion for girls.

We manufacture and retail girls swimwear and fashion in Australia. Our designs are fun loving and funky. I would like to use bright fuschia to match our website www.breezyplum.com.au. We target a higher end market so need it to reflect this.

Industry/Entity Type

Fashion

Contact Information for Business Card

Breezy Plum logo,
Maddie Lorne
(07) 35517204
admin@breezyplum.com.au
www.breezyplum.com.au

Logo Text

Breezy Plum

```html
<!DOCTYPE html>
<html lang="en">
<head>
<meta charset="utf-8">
<title>Breezy Plum – Business Card</title>
<link rel="stylesheet" href="https://fonts.googleapis.com/css2?family=Courier+Prime:wght@700&display=swap">
<style>
  :root {
    --card-bg: #ffffff;
    --page-edge: #f6fbf5;
    --fuchsia: #d93ae6;
    --brand-magenta: #e13fd6;
    --name-blue: #3d6fc9;
    --mint: #72e8c2;
    --sun-yellow: #f6ef52;
    --sea-aqua: #72f2cf;
    --sea-blue: #3a6cc9;
    --sand: #f3f0b8;
    --towel-red: #e83b3b;
  }
  * { margin: 0; padding: 0; box-sizing: border-box; }
  html, body {
    width: 1200px;
    height: 693px;
    overflow: hidden;
    background: var(--page-edge);
  }
  .card {
    position: relative;
    width: 1200px;
    height: 693px;
    background: var(--card-bg);
    font-family: "Courier Prime", "Courier New", monospace;
    font-weight: 700;
  }
  .card__badge {
    position: absolute;
    left: 92px;
    top: 66px;
    width: 446px;
    height: 446px;
  }
  .card__brand {
    position: absolute;
    left: 540px;
    top: 118px;
    width: 620px;
    text-align: center;
    font-size: 92px;
    line-height: 1;
    color: var(--brand-magenta);
    letter-spacing: -2px;
  }
  .card__person {
    position: absolute;
    left: 660px;
    top: 232px;
    font-size: 55px;
    line-height: 1;
    color: var(--name-blue);
  }
  .card__phone {
    position: absolute;
    left: 685px;
    top: 308px;
    font-size: 44px;
    line-height: 1;
    color: var(--name-blue);
  }
  .card__email,
  .card__web {
    position: absolute;
    left: 110px;
    font-size: 47px;
    line-height: 1;
  }
  .card__email { top: 526px; color: var(--mint); }
  .card__web   { top: 584px; color: var(--fuchsia); }
</style>
</head>
<body>
  <main class="card">
    <svg class="card__badge" viewBox="0 0 446 446" role="img" aria-label="Illustration of a girl in a polka-dot swimsuit relaxing on a striped beach towel by the sea">
      <defs>
        <linearGradient id="beachTones" x1="0" y1="0" x2="0" y2="1">
          <stop offset="0" stop-color="var(--sea-aqua)"/>
          <stop offset="0.40" stop-color="var(--sea-aqua)"/>
          <stop offset="0.48" stop-color="var(--sea-blue)"/>
          <stop offset="0.56" stop-color="var(--sea-blue)"/>
          <stop offset="0.64" stop-color="var(--sand)"/>
          <stop offset="1" stop-color="#f4c9c9"/>
        </linearGradient>
      </defs>
      <circle cx="223" cy="223" r="214" fill="url(#beachTones)"/>
      <circle cx="223" cy="223" r="214" fill="none" stroke="var(--sun-yellow)" stroke-width="10"/>
    </svg>

    <h1 class="card__brand">Breezy Plum</h1>
    <p class="card__person">Maddie Lorne</p>
    <p class="card__phone">(07) 35517204</p>

    <p class="card__email">admin@breezyplum.com.au</p>
    <p class="card__web">www.breezyplum.com.au</p>
  </main>
</body>
</html>
```